Business card design needed for elearning/LMS consultant

I'm an elearning and learning management system (LMS) consultant that requires a minimalist, technology/cutting edge, business card. I do not have a logo or colour scheme. I offer clients hands on expertise in 'elearning authouring', 'LMS ecosystems', 'elearning strategy', 'technical implementation', 'mlearning', 'LMS evaluation', 'big data', 'learner analytics' and 'reporting strategy', 'social learning', 'elearning blueprint'. I'm thinking a 'tag cloud' of the above services on the back of the card, with contact details on front, but unsure if it's passe so please don't let it constrain you.

Target Market(s)

C-level executives, learning and development senior management,

Industry/Entity Type

Business

Contact Information for Business Card

Owen Haldric
owen.haldric@mailvane.net
0412 836 197

Requirements
Should not have
• cheesy headshots, overused stockphotos, CLIPART and comic sans ;)

```html
<!DOCTYPE html>
<html lang="en">
<head>
<meta charset="utf-8">
<title>Owen Haldric — e-learning consultant</title>
<link rel="stylesheet" href="https://fonts.googleapis.com/css2?family=Poppins:wght@300;600&display=swap">
<style>
  :root {
    --card-bg: #ffffff;
    --ink-grey: #58595b;
    --accent-blue: #0072bc;
    --accent-pink: #ec008c;
  }
  * { margin: 0; padding: 0; box-sizing: border-box; }
  html, body {
    width: 1200px;
    height: 693px;
    overflow: hidden;
    background: var(--card-bg);
  }
  .card {
    position: relative;
    width: 1200px;
    height: 693px;
    background: var(--card-bg);
    font-family: "Poppins", sans-serif;
    color: var(--ink-grey);
  }
  .brand-mark {
    position: absolute;
    left: 205px;
    top: 238px;
    width: 160px;
    height: 160px;
  }
  .identity {
    position: absolute;
    right: 87px;
    top: 262px;
    text-align: right;
  }
  .identity__name {
    font-weight: 600;
    font-size: 90px;
    line-height: 1;
    letter-spacing: -1px;
    color: var(--ink-grey);
  }
  .identity__role {
    margin-top: 12px;
    font-weight: 300;
    font-size: 42px;
    line-height: 1;
    color: var(--ink-grey);
  }
  .contact {
    position: absolute;
    left: 82px;
    top: 520px;
    list-style: none;
    font-weight: 300;
    font-size: 42px;
    line-height: 1;
    color: var(--ink-grey);
  }
  .contact__item + .contact__item { margin-top: 38px; }
</style>
</head>
<body>
  <main class="card">
    <svg class="brand-mark" viewBox="0 0 160 160" aria-hidden="true">
      <circle cx="80" cy="80" r="80" fill="var(--accent-blue)"/>
    </svg>

    <header class="identity">
      <h1 class="identity__name">Owen Haldric</h1>
      <p class="identity__role">e-learning consultant</p>
    </header>

    <ul class="contact">
      <li class="contact__item">e: owen.haldric@mailvane.net</li>
      <li class="contact__item">t: 0412 836 197</li>
    </ul>
  </main>
</body>
</html>
```